Need simple and modern looking business card with all my information on one side and logo on the other side
Info :
Company name - VELMAR CONSTRUCTION LLC
Company addres- 418 harbor 87th. Dunmoor park ny 10352
Email- velmarllc@tridomail.Com
Company phone number 555-318-6094
Cell number- 555-742-0583
Web site - velmarllc.Com
My name Gerald tomasino

Target Market(s)

Construction , home improvement, remodeling

Industry/Entity Type

Construction

Contact Information for Business Card

It has to be moder but at the same time simple

Font styles to use
Sans Serif

Colors
0255a3
ffffff
000000
f78f20
b1b1b1
9d9d9d
1b1b1b
33a6d7
ec1f27

Requirements
Must have
• My logo on one side maybe with a some kind of background on the other side all my information
Nice to have
• Some kind of background pictures provided by you .PLEASE HAVE ACCOUNT WITH PIXELVAULT WILL NOT PAY ANY EXTRA FEES .
Should not have
• Any kind of hamer, nails,screws, helmets itp. Please do not copy the other designs come up with something new.

```html
<!DOCTYPE html>
<html lang="en">
<head>
<meta charset="utf-8">
<title>Velmar Construction LLC – Business Card</title>
<link rel="stylesheet" href="https://fonts.googleapis.com/css2?family=Montserrat:wght@500;600;700&display=swap">
<style>
  :root {
    --black: #000000;
    --ink: #1b1b1b;
    --white: #ffffff;
    --orange: #f78f20;
    --grey-light: #e6e6e6;
    --stage: #f3f3f3;
  }
  * { margin: 0; padding: 0; box-sizing: border-box; }
  html, body { width: 1200px; height: 900px; overflow: hidden; }
  body {
    background: var(--stage);
    font-family: "Montserrat", Arial, sans-serif;
    position: relative;
  }
  .card {
    position: absolute;
    left: 276px;
    width: 648px;
    height: 348px;
    overflow: hidden;
  }
  .card--front { top: 68px; background: var(--white); }
  .card--back { top: 483px; background: var(--black); }

  .band {
    position: absolute;
    left: 12px;
    width: 617px;
    height: 11px;
  }
  .band--top { top: 14px; background: var(--black); }
  .band--bottom { top: 323px; background: var(--orange); }

  .skyline-decor {
    position: absolute;
    left: 0;
    top: 104px;
    width: 190px;
    height: 236px;
    background: linear-gradient(180deg, var(--grey-light), rgba(230,230,230,0.25));
  }

  .holder { position: absolute; left: 143px; top: 72px; color: var(--ink); }
  .holder__name { font-weight: 700; font-size: 14.5px; letter-spacing: 0.8px; }
  .holder__company { font-weight: 500; font-size: 12.5px; letter-spacing: 0.4px; margin-top: 6px; }

  .brand {
    position: absolute;
    display: flex;
    align-items: center;
    gap: 12px;
  }
  .brand__mark { background: var(--orange); flex: none; }
  .brand__name {
    font-weight: 700;
    line-height: 1;
    letter-spacing: 1px;
  }
  .brand__name span { display: block; }
  .brand--front { right: 22px; top: 98px; }
  .brand--front .brand__mark { width: 26px; height: 26px; }
  .brand--front .brand__name { color: var(--ink); font-size: 40px; }
  .brand--front .brand__name .brand__sub { font-size: 13.2px; letter-spacing: 1.6px; margin-top: 6px; }

  .brand--back { left: 50%; top: 118px; transform: translateX(-50%); }
  .brand--back .brand__mark { width: 34px; height: 34px; }
  .brand--back .brand__name { color: var(--white); font-size: 62px; }
  .brand--back .brand__name .brand__sub { font-size: 20.4px; letter-spacing: 2.4px; margin-top: 10px; }

  .contacts {
    position: absolute;
    right: 20px;
    top: 200px;
    display: grid;
    grid-template-columns: auto auto;
    column-gap: 26px;
    row-gap: 18px;
  }
  .contact {
    display: flex;
    align-items: center;
    gap: 10px;
    font-weight: 600;
    font-size: 12.5px;
    color: var(--ink);
    white-space: nowrap;
  }
  .contact__icon {
    width: 31px;
    height: 31px;
    border: 1.5px solid var(--orange);
    border-radius: 50%;
    display: flex;
    align-items: center;
    justify-content: center;
    flex: none;
  }
  .contact__icon svg { width: 16px; height: 16px; fill: none; stroke: var(--orange); stroke-width: 1.8; stroke-linecap: round; stroke-linejoin: round; }

  .address {
    position: absolute;
    left: 235px;
    top: 313px;
    font-weight: 600;
    font-size: 16px;
    color: var(--ink);
    white-space: nowrap;
  }
</style>
</head>
<body>

<section class="card card--front">
  <div class="band band--top"></div>
  <div class="skyline-decor" role="img" aria-label="Faint light grey skyline decoration"></div>

  <div class="holder">
    <p class="holder__name">GERALD TOMASINO</p>
    <p class="holder__company">VELMAR CONSTRUCTION LLC</p>
  </div>

  <div class="brand brand--front">
    <div class="brand__mark"></div>
    <p class="brand__name"><span>VELMAR</span><span class="brand__sub">CONSTRUCTION LLC</span></p>
  </div>

  <div class="contacts">
    <div class="contact contact--office">
      <span class="contact__icon"><svg viewBox="0 0 24 24"><path d="M5 3h4l2 5-2.5 1.5a11 11 0 0 0 6 6L16 13l5 2v4a2 2 0 0 1-2 2A17 17 0 0 1 3 5a2 2 0 0 1 2-2z"/></svg></span>
      <span>555-318-6094</span>
    </div>
    <div class="contact contact--email">
      <span class="contact__icon"><svg viewBox="0 0 24 24"><rect x="3" y="6" width="18" height="13" rx="1"/><path d="M3 7l9 7 9-7"/></svg></span>
      <span>velmarllc@tridomail.com</span>
    </div>
    <div class="contact contact--cell">
      <span class="contact__icon"><svg viewBox="0 0 24 24"><rect x="7" y="2" width="10" height="20" rx="2"/><path d="M11 18h2"/></svg></span>
      <span>555-742-0583</span>
    </div>
    <div class="contact contact--web">
      <span class="contact__icon"><svg viewBox="0 0 24 24"><circle cx="12" cy="12" r="9"/><path d="M3 12h18M12 3a14 14 0 0 1 0 18M12 3a14 14 0 0 0 0 18"/></svg></span>
      <span>velmarllc.Com</span>
    </div>
  </div>

  <p class="address">418 Harbor 87th. Dunmoor Park NY 10352</p>
</section>

<section class="card card--back">
  <div class="brand brand--back">
    <div class="brand__mark"></div>
    <p class="brand__name"><span>VELMAR</span><span class="brand__sub">CONSTRUCTION LLC</span></p>
  </div>
  <div class="band band--bottom"></div>
</section>

</body>
</html>
```